Willowmere Chiropractic 20th Birthday Party

We are a holistic health practice focussing on women's children's health and we need a poster and an invitation to our 20th birthday celebration.

On Sat Nov 24th 12-3pm at WCC

```html
<!DOCTYPE html>
<html lang="en">
<head>
<meta charset="utf-8">
<title>Willowmere Chiropractic Centre – 20th Birthday Celebration</title>
<link rel="stylesheet" href="https://fonts.googleapis.com/css2?family=Montserrat:wght@600&family=Playfair+Display:wght@700&display=swap">
<style>
  :root {
    --blush-light: #fbdcd6;
    --blush-mid: #f6c7c0;
    --blush-deep: #f1b5ad;
    --ink: #5e5e5e;
    --white: #ffffff;
    --teal: #5cc5bf;
  }
  html, body {
    margin: 0;
    padding: 0;
    width: 1200px;
    height: 1200px;
    overflow: hidden;
  }
  .poster {
    position: relative;
    width: 1200px;
    height: 1200px;
    overflow: hidden;
    font-family: "Montserrat", Arial, sans-serif;
    color: var(--ink);
  }
  .wash {
    position: absolute;
    inset: 0;
    background:
      radial-gradient(ellipse 520px 380px at 78% 22%, var(--blush-deep) 0%, transparent 70%),
      radial-gradient(ellipse 600px 420px at 20% 70%, var(--blush-mid) 0%, transparent 72%),
      radial-gradient(ellipse 480px 360px at 60% 55%, rgba(241,181,173,0.55) 0%, transparent 70%),
      linear-gradient(160deg, var(--blush-light) 0%, var(--blush-mid) 55%, var(--blush-light) 100%);
  }
  .graphics {
    position: absolute;
    inset: 0;
    width: 1200px;
    height: 1200px;
  }
  .numeral {
    font-family: "Playfair Display", Georgia, serif;
    font-weight: 700;
    fill: var(--white);
  }
  .plus { fill: var(--white); }
  .headline {
    position: absolute;
    left: 717px;
    top: 66px;
    margin: 0;
    font-size: 32px;
    font-weight: 600;
    line-height: 57px;
    letter-spacing: 0.3em;
    text-transform: uppercase;
  }
  .headline span { display: block; }
  .divider {
    position: absolute;
    left: 737px;
    top: 422px;
    width: 148px;
    height: 14px;
    background: var(--ink);
  }
  .details {
    position: absolute;
    right: 515px;
    top: 893px;
    margin: 0;
    text-align: right;
    font-size: 32px;
    font-weight: 600;
    line-height: 57px;
    letter-spacing: 0.3em;
    margin-right: -0.3em;
    text-transform: uppercase;
  }
  .details span { display: block; }
  .brand {
    position: absolute;
    left: 1009px;
    top: 1014px;
    width: 191px;
    height: 186px;
    background: var(--teal);
    display: flex;
    align-items: center;
    justify-content: center;
    text-align: center;
    color: var(--white);
    font-family: "Montserrat", Arial, sans-serif;
    font-weight: 600;
    font-size: 21px;
    line-height: 1.25;
  }
</style>
</head>
<body>
  <main class="poster">
    <div class="wash" role="img" aria-label="Soft pink watercolour wash background"></div>

    <svg class="graphics" viewBox="0 0 1200 1200" aria-hidden="true">
      <text class="numeral" x="20" y="612" font-size="860">2</text>
      <text class="numeral" x="590" y="1230" font-size="860">0</text>

      <g class="plus">
        <rect x="148" y="-30" width="26" height="100"/><rect x="111" y="8" width="100" height="26"/>
        <rect x="32" y="154" width="26" height="100"/><rect x="-5" y="191" width="100" height="26"/>
        <rect x="1133" y="416" width="26" height="100"/><rect x="1096" y="453" width="100" height="26"/>
        <rect x="779" y="817" width="22" height="76"/><rect x="752" y="844" width="76" height="22"/>
        <rect x="44" y="925" width="26" height="100"/><rect x="7" y="962" width="100" height="26"/>
        <rect x="383" y="1130" width="26" height="100"/><rect x="346" y="1167" width="100" height="26"/>
      </g>
    </svg>

    <h1 class="headline">
      <span>Birthday</span>
      <span>Celebration</span>
      <span>for</span>
      <span>Willowmere</span>
      <span>Chiropractic</span>
      <span>Centre</span>
    </h1>
    <div class="divider"></div>

    <p class="details">
      <span>Nov 24, Saturday</span>
      <span>12-3pm</span>
      <span>2 Hartley St</span>
      <span>Brambleton</span>
    </p>

    <div class="brand">Willowmere<br>Chiropractic</div>
  </main>
</body>
</html>
```